Please create a custom website design for Harbor Links Institute.

We need a 2 page design.

1. page
Home

Blue Logo
Headline: Home, instructors, Programs, Teaching Video
Club reviews, Event, Member's area, Contact & Location

Please combine 3 coaches golf swing (attached) to one big picture and use other background maybe a golf course or something

3-4 video thumbnails links(Photo attached)
title: About Harbor links,Instrutional video, Club reviews, Event etc.

Welcome to harbor links......
Members Voice

Footline:
Partners Vorcane, Swingly, KEV rollbay...etc

2. page

Instructors (Photo attached )

Martin Lobb (Blue shirt) Photo + 1 video Thumbnail
Founder/ Director
KSGF Tour Pro/Teaching Pro (A)
NRWCA Lv 3 Certified Instrutor
Trained at Oswin Falk School of Golf
Trained at Japan Kawabeyama Country club
Tarwick University of Technology

Dara Pollen (white shirt) Photo + 1 video Thumbnail
Teaching Director/Head Coach
Teaching Director/Head coach
- Member of Continental SGU
Member of Germany SGU
Member of UK SGU
NRWCA Lv3 Certified Instructor
Europe Rising Circuit(1999-02)

Pavel Ortiz(black shirt) Photo + 1 video Thumbnail

KSGF Teaching Pro (A)
KSGF National Mentor Shield Champion2014
Ridgeway Golf College Australia

The logo is attached to this brief.

Preferred colours could be based on Blue
Here is the link to the logo project: http://briefs.plorvex.com/task.aspx?id=413657

Target Market(s)

Golfers

Industry/Entity Type

Golf Course

Number of Pages Required

2 page

Font styles to use
Sans Serif

Colors
0555a3
ffffff
ec2027

Requirements
Must have
• The photos provided
• Blue based Webpage
Nice to have
• Other golf photos
• a little touch of red color

```html
<!DOCTYPE html>
<html lang="en">
<head>
<meta charset="utf-8">
<title>Harbor Links Institute</title>
<link href="https://fonts.googleapis.com/css2?family=Open+Sans:wght@400;600;700&family=Raleway:wght@500;600;700&display=swap" rel="stylesheet">
<style>
:root{
  --blue:#0555a3;
  --blue-dark:#043d78;
  --red:#ec2027;
  --white:#ffffff;
  --ink:#1c1f24;
  --bar:#15181c;
  --panel:rgba(20,24,30,.72);
  --card:rgba(60,64,70,.78);
}
*{margin:0;padding:0;box-sizing:border-box}
html,body{width:1200px;height:2576px;overflow:hidden;background:var(--ink)}
body{font-family:"Open Sans",Arial,sans-serif;color:var(--white);position:relative}
.topbar{position:absolute;top:0;left:0;width:1200px;height:32px;background:var(--bar);display:flex;justify-content:space-between;align-items:center;padding:0 40px;font-size:14px}
.topbar .auth{font-weight:600;letter-spacing:.5px}
.hero{position:absolute;top:32px;left:0;width:1200px;height:788px;background:radial-gradient(ellipse at 50% 10%,#f3e9b9 0%,#b8c67a 22%,transparent 45%),linear-gradient(180deg,#7d9a4f 0%,#55812e 40%,#3f6e22 70%,#2d5318 100%)}
.brand{position:absolute;top:100px;left:480px;width:240px;height:240px;border-radius:50%;background:var(--blue);border:10px solid var(--white);display:flex;flex-direction:column;align-items:center;justify-content:center;box-shadow:0 6px 18px rgba(0,0,0,.35)}
.brand span{font-family:"Raleway",sans-serif;font-weight:700;font-size:30px;line-height:1.15;text-align:center;color:var(--white)}
.mainnav{position:absolute;top:460px;left:140px;display:flex;gap:4px}
.mainnav a{width:128px;height:160px;background:var(--blue);color:var(--white);text-decoration:none;display:flex;flex-direction:column;align-items:center;justify-content:flex-end;padding-bottom:26px;font-size:17px;gap:18px;text-align:center;line-height:1.3}
.mainnav a.active{background:var(--white);color:var(--blue)}
.mainnav svg{width:44px;height:44px}
.pointer{position:absolute;top:720px;left:540px;width:120px;height:110px}
.strip{position:absolute;top:820px;left:0;width:1200px;height:180px;border-top:6px solid var(--blue);display:flex}
.strip .thumb{width:300px;height:174px}
.t1{background:linear-gradient(160deg,#d9d9d9,#8a8a8a)}
.t2{background:linear-gradient(160deg,#c9c2b6,#6f6a62)}
.t4{background:linear-gradient(160deg,#bcc3c9,#5d6670)}
.strip .feature{width:300px;height:174px;background:var(--blue);display:flex;flex-direction:column;align-items:center;justify-content:center;gap:22px}
.feature h3{font-family:"Raleway",sans-serif;font-size:26px;font-weight:600}
.play{width:44px;height:44px;border-radius:50%;background:var(--ink);display:flex;align-items:center;justify-content:center}
.welcome{position:absolute;top:1000px;left:0;width:1200px;height:732px;background:linear-gradient(180deg,#a9b9c6 0%,#8ea1ae 30%,#6f8a62 62%,#4f6f3a 100%)}
.welcome-box{position:absolute;top:272px;left:180px;width:840px;height:348px;background:var(--panel);text-align:center;padding:42px 90px}
.welcome-box h1{font-family:"Raleway",sans-serif;font-size:46px;font-weight:600;margin-bottom:24px}
.welcome-box p{font-size:17px;line-height:1.45;margin-bottom:30px}
.btn{display:inline-block;background:var(--blue);color:var(--white);font-size:15px;font-weight:700;padding:12px 34px;text-decoration:none;text-transform:uppercase}
.btn.dark{background:var(--ink)}
.services{position:absolute;top:1732px;left:0;width:1200px;height:630px;border-top:8px solid var(--blue);background:linear-gradient(180deg,#6f8c56 0%,#4c6e34 45%,#6f9446 80%,#87a852 100%)}
.cards{position:absolute;top:108px;left:140px;display:flex;gap:20px}
.card{width:300px;height:472px;background:var(--card);padding:24px 24px;text-align:center}
.card h2{font-family:"Raleway",sans-serif;font-size:24px;font-weight:600;margin-bottom:16px}
.card .pic{height:200px;margin-bottom:18px}
.p1{background:linear-gradient(170deg,#9cc3e6,#c9b08c 60%,#5f8b3c)}
.p2{background:linear-gradient(170deg,#b7cfe0,#7fae52 55%,#3f7a2a)}
.p3{background:linear-gradient(170deg,#8fb8e2,#6f9d48 60%,#3e6e25)}
.card p{font-size:13px;line-height:1.45;margin-bottom:26px}
.card .btn{font-size:12px;padding:9px 28px}
.footer{position:absolute;top:2362px;left:0;width:1200px;height:214px;background:var(--bar)}
.footer .mark{position:absolute;top:12px;left:552px;width:96px;height:96px;border-radius:50%;background:var(--blue);border:5px solid var(--white);display:flex;align-items:center;justify-content:center;font-family:"Raleway",sans-serif;font-weight:700;font-size:12px;text-align:center;line-height:1.15}
.footnav{position:absolute;top:116px;left:40px;font-size:15px}
.footnav a{color:var(--white);text-decoration:none}
.footnav a.active{color:var(--blue)}
.copy{position:absolute;top:162px;left:40px;font-size:13px;color:#c9cdd2}
.partners{position:absolute;top:98px;left:900px;display:flex;gap:14px}
.partner{width:80px;height:48px;border-radius:4px;background:var(--blue)}
</style>
</head>
<body>
<header class="topbar">
  <span class="email">info@harborlinksmail.com</span>
  <span class="auth">SIGN IN &nbsp;|&nbsp; SIGNUP</span>
</header>

<section class="hero" role="img" aria-label="Sunlit golf course with a golfer's club and a ball on the tee">
  <div class="brand"><span>Harbor Links<br>Institute</span></div>
  <nav class="mainnav">
    <a href="#"><svg viewBox="0 0 24 24" fill="#fff"><path d="M12 3 2 12h3v8h5v-5h4v5h5v-8h3z"/></svg>Home</a>
    <a href="#" class="active"><svg viewBox="0 0 24 24" fill="#0555a3"><circle cx="6" cy="8" r="3"/><circle cx="12" cy="7" r="3"/><circle cx="18" cy="8" r="3"/><path d="M1 18c0-4 3-6 5-6s3 1 3 1-1 2-1 5zM7 18c0-4 3-6 5-6s5 2 5 6zM23 18c0-4-3-6-5-6s-3 1-3 1 1 2 1 5z"/></svg>Instructors</a>
    <a href="#"><svg viewBox="0 0 24 24" fill="#fff"><path d="M6 19a5 5 0 0 1-.5-10A7 7 0 0 1 19 9a5 5 0 0 1 0 10z"/></svg>Programs</a>
    <a href="#"><svg viewBox="0 0 24 24" fill="none" stroke="#fff" stroke-width="2"><rect x="3" y="4" width="18" height="16"/><path d="M10 9l5 3-5 3z" fill="#fff"/></svg>Teaching<br>Video</a>
    <a href="#"><svg viewBox="0 0 24 24" fill="#fff"><path d="M2 4h13v9H7l-4 3v-3H2z"/><path d="M17 8h5v9h-1v3l-4-3h-6v-2h6z"/></svg>Club<br>Reviews</a>
    <a href="#"><svg viewBox="0 0 24 24" fill="none" stroke="#fff" stroke-width="2"><rect x="3" y="5" width="18" height="16"/><path d="M3 10h18M8 2v5M16 2v5"/><path d="M12 13v5M9.5 15.5h5"/></svg>Event</a>
    <a href="#"><svg viewBox="0 0 24 24" fill="#fff"><path d="M6 3h4l1 5-2 1a12 12 0 0 0 6 6l1-2 5 1v4a2 2 0 0 1-2 2C10 20 4 14 4 5a2 2 0 0 1 2-2z"/></svg>Contact</a>
  </nav>
  <svg class="pointer" viewBox="0 0 120 110"><path d="M0 0h40l20 28L80 0h40v110H0z" fill="#0555a3"/><circle cx="60" cy="52" r="10" fill="#fff"/><path d="M57 48l7 4-7 4z" fill="#0555a3"/></svg>
</section>

<section class="strip">
  <div class="thumb t1" role="img" aria-label="Video thumbnail: golfer at address"></div>
  <div class="thumb t2" role="img" aria-label="Video thumbnail: instructors on the course"></div>
  <div class="feature">
    <h3>Title Here</h3>
    <div class="play"><svg width="16" height="16" viewBox="0 0 16 16"><path d="M4 2l10 6-10 6z" fill="#fff"/></svg></div>
  </div>
  <div class="thumb t4" role="img" aria-label="Video thumbnail: golfer swinging by the lake"></div>
</section>

<section class="welcome" role="img" aria-label="Golfer in follow-through against mountains and sky">
  <div class="welcome-box">
    <h1>Welcome To Harbor Links</h1>
    <p>Lorem Ipsum is simply dummy text of the printing and typesetting industry. Lorem Ipsum has been the industry's standard dummy text</p>
    <a href="#" class="btn">Read More</a>
  </div>
</section>

<section class="services" role="img" aria-label="Golf course with tall trees in the background">
  <div class="cards">
    <article class="card">
      <h2>Service 01</h2>
      <div class="pic p1" role="img" aria-label="Golfer holding a club on a sunny course"></div>
      <p>Our coaches shape a clear plan for every swing, guiding steady progress from first lesson to game day.</p>
      <a href="#" class="btn">Read More</a>
    </article>
    <article class="card">
      <h2>Service 02</h2>
      <div class="pic p2" role="img" aria-label="Golf ball and club on the green"></div>
      <p>Short game clinics sharpen putting, chipping and bunker play with drills built for real course moments.</p>
      <a href="#" class="btn dark">Read More</a>
    </article>
    <article class="card">
      <h2>Service 03</h2>
      <div class="pic p3" role="img" aria-label="Golf bag standing on the fairway"></div>
      <p>Club fitting and video review help each player find the right gear and a repeatable swing fast.</p>
      <a href="#" class="btn">Read More</a>
    </article>
  </div>
</section>

<footer class="footer">
  <div class="mark">Harbor<br>Links</div>
  <nav class="footnav">
    <a href="#">Home</a> | <a href="#" class="active">Instructors</a> | <a href="#">Programs</a> | <a href="#">Teaching Video</a> | <a href="#">Club Reviews</a> | <a href="#">Event</a> | <a href="#">Member's area</a> | <a href="#">Contact &amp; Location</a>
  </nav>
  <p class="copy">© 2014 Harbor links All rights reserved</p>
  <div class="partners" aria-label="Partner badges">
    <div class="partner"></div>
    <div class="partner"></div>
    <div class="partner"></div>
  </div>
</footer>
</body>
</html>
```